Calder Mindworks Psychology website transfer from WIX to Wordpress

I have a website currently coded in WIX and I want it (or something like it or better) designed to be coded on Wordpress instead. The website should have mobile optimization so that it can be viewed on mobile devices.

The current website is at: www.caldermindworks.example

I'm not looking for versions of the website that are very different to what I already have, unless they improve on it aesthetically. I'm mainly looking to have a Wordpress version of this website that I built, away from the WIX ecosystem.

Target Market(s)

Psychology services clients

Coding

Coded - Design and coding required

Number of Pages Required

5+ page

Font styles to use
Serif

Requirements
Must have
• The finished product shoud match my website exactly.
Nice to have
• I'm happy to see new ideas that improve on the current website.
Should not have
• It should not be a different version of my website.

```html
<!DOCTYPE html>
<html lang="en">
<head>
<meta charset="utf-8">
<title>Calder Mindworks Psychology</title>
<link href="https://fonts.googleapis.com/css2?family=Inter:wght@400;500;600;700&family=Cedarville+Cursive&display=swap" rel="stylesheet">
<style>
:root{
  --green:#2f5a4d;
  --green-dark:#244a3e;
  --ink:#1c1c1c;
  --body:#4a4a4a;
  --mist:#eceeed;
  --sand:#f6f5f2;
  --white:#fff;
  --black:#000;
}
*{box-sizing:border-box;margin:0;padding:0}
html,body{width:1200px;height:4351px;overflow:hidden}
body{position:relative;background:var(--white);font-family:"Inter",sans-serif;color:var(--ink)}
.abs{position:absolute}
.script{font-family:"Cedarville Cursive",cursive;font-weight:400}
.ph{position:absolute}
.btn{position:absolute;display:flex;align-items:center;justify-content:center;background:var(--green);color:var(--white);font-weight:500;font-size:16px}
.brand{font-weight:600;color:var(--green);font-size:19px;display:flex;align-items:center;gap:10px}
.brand i{width:14px;height:14px;background:var(--green);display:block}

/* header */
.nav{top:31px;left:472px;display:flex;gap:36px;font-size:15.5px;color:var(--ink)}
.nav .active{color:var(--green);font-weight:600;text-decoration:underline;text-underline-offset:6px}

/* hero */
.hero-panel{left:0;top:125px;width:540px;height:462px;background:var(--green);color:var(--white);padding:70px 0 0 98px}
.hero-panel .brand{color:var(--white)}
.hero-panel .brand i{background:var(--white)}
.hero-panel h1{font-size:54px;margin-top:28px;line-height:1.2}
.hero-panel p{font-size:14.5px;line-height:28px;margin-top:18px;width:400px}
.ghost{border:1.5px solid var(--white);color:var(--white);background:none;font-size:15px}

/* healing */
.heal{left:164px;top:730px;width:872px;height:168px;border:2px solid var(--green)}
.heal h2{position:absolute;left:40px;top:32px;font-size:54px;font-weight:500;white-space:nowrap}
.heal h2 span{color:var(--green);font-size:56px}

/* about */
.about-copy{left:618px;top:1098px;width:490px}
.about-copy h2{font-size:34px;font-weight:600}
.about-copy h2 span{color:var(--green);font-size:38px;font-weight:400}
.about-copy h3{color:var(--green);font-size:17px;font-weight:500;line-height:30px;margin-top:16px}
.about-copy p{font-size:13px;line-height:28.5px;color:var(--body);margin-top:12px}

/* carousel */
.card-cap{top:2117px;width:228px;text-align:center;font-size:17px;font-weight:600;line-height:29px}
.arrow{width:26px;height:26px;border:1.5px solid #777;border-radius:50%;display:flex;align-items:center;justify-content:center}

/* clinical */
.clin-copy{left:98px;top:2340px;width:480px}
.clin-copy h2{font-size:32px;font-weight:500;line-height:42px}
.clin-copy h2 span{color:var(--green);font-size:34px}
.clin-copy p{font-size:14.5px;line-height:30px;color:var(--body);margin-top:14px}

/* services */
.svc{top:2946px;width:320px;height:363px;border:2px solid #e6e6e6;text-align:center;padding:0 18px}
.svc .dia{width:76px;height:76px;background:var(--green);transform:rotate(45deg);margin:42px auto 0;display:flex;align-items:center;justify-content:center}
.svc h3{color:var(--green);font-size:21px;font-weight:600;margin-top:42px}
.svc p{font-size:14px;line-height:28.5px;color:var(--body);margin-top:18px}

/* acknowledgement */
.ack{left:0;top:3420px;width:1200px;height:485px;background:var(--sand)}
.ack p{position:absolute;font-size:14.5px;line-height:30px;color:var(--body)}
.flag{width:98px;height:72px;border:1px solid #ddd;background:var(--white);padding:12px}
.flag div{width:100%;height:100%}

/* footer */
.foot{left:0;top:3905px;width:1200px;height:446px;background:var(--black);color:var(--white)}
.foot h4{position:absolute;font-size:22px;font-weight:500;line-height:34px}
.foot .list{position:absolute;font-size:14px;line-height:28px}
.soc{width:32px;height:32px;border-radius:50%;background:var(--green)}
</style>
</head>
<body>

<!-- header -->
<div class="abs brand" style="left:97px;top:30px">Calder Mindworks Psychology</div>
<nav class="abs nav"><span class="active">Home</span><span>FAQs</span><span>About</span><span>Services</span><span>Fees &amp; Rebates</span></nav>
<div class="btn" style="left:967px;top:17px;width:133px;height:51px">Contact Us</div>

<!-- hero -->
<div class="ph" role="img" aria-label="Photo of a smiling family of three sitting together on a living room floor" style="left:445px;top:88px;width:755px;height:534px;background:linear-gradient(120deg,#dfe1dc 0%,#b7a896 45%,#6f7f95 100%)"></div>
<section class="abs hero-panel">
  <div class="brand"><i></i>Calder Mindworks Psychology</div>
  <h1 class="script">Welcome To</h1>
  <p>Clinical and Counselling Psychologist | Accredited Sex Therapist | LGBTQIA+ and <span class="script">Neurodivergence activist</span> | Clinical Trainer and Consultant.</p>
  <div class="btn ghost" style="left:98px;top:342px;width:135px;height:48px">Learn More</div>
</section>

<!-- healing -->
<div class="abs heal"><h2>Finding Healing <span class="script">After Trauma</span></h2></div>
<div class="btn" style="left:443px;top:872px;width:314px;height:51px;font-size:15px;font-weight:600">SCHEDULE A FREE CONSULTATION</div>

<!-- about -->
<div class="abs" style="left:0;top:1040px;width:475px;height:698px;background:var(--mist)"></div>
<div class="ph" role="img" aria-label="Photo of the psychologist in a flat cap writing notes in an armchair" style="left:98px;top:1107px;width:475px;height:566px;background:linear-gradient(160deg,#e9e6e1 0%,#b34a2c 50%,#4d443c 100%)"></div>
<div class="abs about-copy">
  <h2>Dr Elio <span class="script">Marsh</span></h2>
  <h3>Clinical and Counselling Psychologist<br>Clinical Psychosexual Therapist</h3>
  <p>My name is Elio (he/they) and I am a Clinical and Counselling Psychologist, and accredited Clinical Psychosexual Therapist, with over 15 years' experience working with adults and young people of all abilities and identities.My practice focuses on sex therapy and working with diversity, which regularly includes supporting members of LGBTQIA+, neurodivergent, and disabled communities. Because of this work, I am sex-positive and kink-, polyamory-, LGBTQIA+ and neurodiversity knowledgeable and affirming in my practice. I am also a member of many lived experience communities as part of my commitment to lifelong learning and honoring lived experience.I know that seeing a therapistsuch, I always aim to curate a non-judgmental, collaborative, and intentional approach to working with people toward their personal goals and a life of value.</p>
</div>
<div class="btn" style="left:619px;top:1628px;width:133px;height:46px">Learn More</div>

<!-- carousel -->
<div class="abs arrow" style="left:41px;top:1959px"><svg width="10" height="10" viewBox="0 0 10 10"><path d="M6.5 1.5 3 5l3.5 3.5" fill="none" stroke="#777" stroke-width="1.5"/></svg></div>
<div class="abs arrow" style="left:1138px;top:1959px;border-color:#222"><svg width="10" height="10" viewBox="0 0 10 10"><path d="M3.5 1.5 7 5 3.5 8.5" fill="none" stroke="#222" stroke-width="1.5"/></svg></div>
<div class="ph" role="img" aria-label="Photo of two people embracing" style="left:98px;top:1841px;width:228px;height:260px;background:linear-gradient(150deg,#5a5f52,#8b6b62)"></div>
<div class="ph" role="img" aria-label="Photo of an older couple laughing together outdoors" style="left:357px;top:1841px;width:228px;height:260px;background:linear-gradient(150deg,#6f7a5e,#9a8e86)"></div>
<div class="ph" role="img" aria-label="Photo of two people lying face to face" style="left:615px;top:1841px;width:228px;height:260px;background:linear-gradient(150deg,#4e4a48,#7a6a63)"></div>
<div class="ph" role="img" aria-label="Photo of two men embracing and smiling" style="left:873px;top:1841px;width:228px;height:260px;background:linear-gradient(150deg,#6b6b68,#8f7f72)"></div>
<div class="abs card-cap" style="left:98px">Sexual &amp; Interpersonal Trauma</div>
<div class="abs card-cap" style="left:357px">Intimacy &amp; Connection</div>
<div class="abs card-cap" style="left:615px">Mismatched Libido &amp; Sex 'Addiction'</div>
<div class="abs card-cap" style="left:873px">Internalised Shame &amp; Discrimination</div>

<!-- clinical -->
<div class="abs" style="left:0;top:2257px;width:1200px;height:590px;background:var(--mist)"></div>
<div class="abs clin-copy">
  <h2>What is a Clinical<br><span class="script">Psychosexual Therapist?</span></h2>
  <p>Sometimes referred to as a sex therapist, a Clinical Psychosexual Therapist is someone who has postgraduate university qualifications in the field of human sexuality, which is a broad area encompassing subjects like:</p>
  <p style="margin-top:30px">sexual orientation, gender identity, sexual function and diversity, sexual and reproductive health, intersectional feminism, relationship dynamics, and sexual trauma.</p>
</div>
<div class="btn" style="left:98px;top:2704px;width:454px;height:48px;justify-content:flex-start;padding-left:22px;font-size:15.5px">How can a clinical psychosexual therapist help me?&nbsp;|</div>
<div class="abs" style="left:958px;top:2327px;width:154px;height:140px;background:var(--green)"></div>
<div class="abs" style="left:652px;top:2340px;width:440px;height:422px;background:var(--green)"></div>
<div class="ph" role="img" aria-label="Portrait photo of the psychologist smiling in a flat cap and plaid shirt" style="left:665px;top:2332px;width:437px;height:414px;border:9px solid var(--white);background:linear-gradient(160deg,#f4f2ee 0%,#a37a5c 55%,#7a3b2c 100%)"></div>

<!-- services -->
<div class="abs svc" style="left:97px">
  <div class="dia"><svg width="34" height="34" viewBox="0 0 34 34" style="transform:rotate(-45deg)"><circle cx="17" cy="12" r="6" fill="none" stroke="#fff" stroke-width="1.6"/><path d="M6 30c1-7 6-10 11-10s10 3 11 10" fill="none" stroke="#fff" stroke-width="1.6"/></svg></div>
  <h3>Psychological Therapy</h3>
  <p>Psychological assessment, education, counselling, and therapy using person-centered and evidence-based integrative therapeutic interventions.</p>
</div>
<div class="abs svc" style="left:440px">
  <div class="dia"><svg width="34" height="34" viewBox="0 0 34 34" style="transform:rotate(-45deg)"><rect x="5" y="7" width="24" height="16" fill="none" stroke="#fff" stroke-width="1.6"/><path d="M17 23v6M11 29h12" stroke="#fff" stroke-width="1.6"/></svg></div>
  <h3>Clinical Supervision</h3>
  <p>Clinical supervision to support provisional psychologists and registrars, early career mentoring, technical skill building, and clinical case discussion.</p>
</div>
<div class="abs svc" style="left:782px">
  <div class="dia"><svg width="34" height="34" viewBox="0 0 34 34" style="transform:rotate(-45deg)"><circle cx="9" cy="24" r="4" fill="none" stroke="#fff" stroke-width="1.6"/><circle cx="25" cy="24" r="4" fill="none" stroke="#fff" stroke-width="1.6"/><circle cx="17" cy="10" r="4" fill="none" stroke="#fff" stroke-width="1.6"/></svg></div>
  <h3>Training and Consultancy</h3>
  <p>Training for general psychology or special interest subjects like sexology and neurodivergence, and consultancy for practices and organisations.</p>
</div>
<div class="btn" style="left:194px;top:3286px;width:126px;height:41px;font-size:14px">Learn More</div>
<div class="btn" style="left:537px;top:3286px;width:126px;height:41px;font-size:14px">Learn More</div>
<div class="btn" style="left:879px;top:3286px;width:126px;height:41px;font-size:14px">Learn More</div>

<!-- acknowledgement -->
<section class="abs ack">
  <p style="left:98px;top:80px;width:475px">We acknowledge the Traditional Custodians of the lands upon which we work here in Meanjin, the Turrbal and Jaggera people, as the first inhabitants of our nation. We recognise their continuing connection to land, water, and culture and pay our respects to their Elders past, present, and emerging - as well as First Nations people and the stolen generation who have yet to find their home. Their lands never ceded sovereignty. Always was, always will be, Aboriginal land.</p>
  <p style="left:630px;top:106px;width:475px">At Calder Mindworks Psychology, we welcome people of all backgrounds, race, ethnicity, genders, sexuality, relationship type, neurotype, and abilities.<br>Please contact us if we can assist you to make your appointment more inclusive in any way or provide us feedback on how we can do better.</p>
  <div class="abs flag" style="left:98px;top:338px"><div role="img" aria-label="Aboriginal flag" style="background:linear-gradient(#111 50%,#c8102e 50%)"></div></div>
  <div class="abs flag" style="left:210px;top:338px"><div role="img" aria-label="Torres Strait Islander flag" style="background:linear-gradient(#0a8a3a 20%,#1f2a8a 20% 80%,#0a8a3a 80%)"></div></div>
  <div class="abs flag" style="left:630px;top:310px"><div role="img" aria-label="Progress pride flag" style="background:linear-gradient(#e40303,#ff8c00,#ffed00,#008026,#004dff,#750787)"></div></div>
  <div class="abs flag" style="left:743px;top:310px"><div role="img" aria-label="Inclusive pride flag" style="background:linear-gradient(135deg,#5bcefa,#f5a9b8,#444)"></div></div>
  <div class="abs flag" style="left:862px;top:310px"><div role="img" aria-label="Neurodiversity flag" style="background:linear-gradient(#e94d3f,#f5a623,#f8e71c,#7ed321)"></div></div>
</section>

<!-- footer -->
<footer class="abs foot">
  <div class="abs brand" style="left:60px;top:105px;color:var(--white)"><i style="background:var(--green)"></i>Calder Mindworks<br>Psychology</div>
  <div class="abs soc" style="left:94px;top:197px"></div>
  <div class="abs soc" style="left:143px;top:197px"></div>
  <div class="abs soc" style="left:192px;top:197px"></div>
  <div class="abs soc" style="left:241px;top:197px"></div>
  <h4 style="left:350px;top:92px">Practice Hours<br>(by appointment only):</h4>
  <svg class="abs" style="left:352px;top:180px" width="32" height="32" viewBox="0 0 32 32"><circle cx="16" cy="16" r="16" fill="#2f5a4d"/><circle cx="16" cy="16" r="8" fill="none" stroke="#fff" stroke-width="1.6"/><path d="M16 11v5l3 2" fill="none" stroke="#fff" stroke-width="1.6"/></svg>
  <div class="list" style="left:397px;top:172px;font-size:15px;line-height:34px">Mondays:<br>9:30am - 3:30pm<br>Thursdays:<br>8:30am - 2:30pm</div>
  <h4 style="left:642px;top:92px">Appointments or after hour<br>Please consider Contacting:</h4>
  <div class="list" style="left:645px;top:168px">Careline on 13 20 41<br>Youth Talkline on 1800 402 615<br>MenSpeak Line on 1300 512 337<br>Crisis Callback on 1300 720 158</div>
  <div class="list" style="left:934px;top:168px">Clear Skies on 1300 61 72 09<br>Headroom on 1800 337 214<br>PrideLine on 1800 906 352<br>YarnCall on 13 48 50</div>
  <div class="abs" style="left:48px;top:408px;width:1104px;height:1px;background:#555"></div>
  <div class="abs" style="left:0;top:420px;width:1200px;text-align:center;font-size:14px">Copyrights@2024.Calder Mindworks Psychology.All Rights Reserved</div>
</footer>

</body>
</html>
```